Business card for exciting VC company

Should look simple, crisp, and modern.

Industry/Entity Type

Venture Capital

Contact Information for Business Card

Would like to see at least one design that has our blue on the back with the tagline "Transforming Traditional Industry" and white front with contact details.

Font styles to use
Sans Serif

Requirements
Must have
• Logo

Gregory Tallis
gtallis@brindlewave.vc
Managing Partner
M (628)354-xxxx

```html
<!DOCTYPE html>
<html lang="en">
<head>
<meta charset="utf-8">
<title>Brindlewave Capital – Business Card</title>
<link rel="stylesheet" href="https://fonts.googleapis.com/css2?family=Lato:wght@400;700&display=swap">
<style>
  :root {
    --brand-blue: #4383c6;
    --ink: #151515;
    --paper: #ffffff;
    --backdrop: #d1d1cd;
    --text-dark: #1f1f1f;
  }
  * { box-sizing: border-box; margin: 0; padding: 0; }
  html, body {
    width: 1200px; height: 801px; overflow: hidden;
    background: var(--backdrop);
    font-family: "Lato", sans-serif;
  }
  .stage { position: relative; width: 1200px; height: 801px; }
  .card {
    position: absolute;
    width: 520px; height: 297px;
    box-shadow: 0 10px 28px rgba(0,0,0,0.18);
  }
  .card-front { left: 50px; top: 130px; background: var(--paper); }
  .card-back { left: 630px; top: 374px; background: var(--brand-blue); }

  .wordmark {
    position: absolute; left: 0; right: 0;
    text-align: center;
    font-weight: 700;
    letter-spacing: 0.12em;
    text-transform: uppercase;
    white-space: nowrap;
  }
  .card-front .wordmark { top: 62px; font-size: 30px; color: var(--ink); }
  .card-back .wordmark { top: 104px; font-size: 32px; color: var(--ink); }

  .holder {
    position: absolute; left: 46px; top: 180px;
  }
  .holder-name {
    font-size: 24px; font-weight: 700; color: var(--brand-blue);
  }
  .holder-title {
    font-size: 15px; color: var(--text-dark); margin-top: 2px;
  }
  .divider {
    position: absolute; left: 282px; top: 172px;
    width: 1.5px; height: 78px; background: var(--brand-blue);
  }
  .contacts {
    position: absolute; left: 304px; top: 172px;
    list-style: none;
  }
  .contacts li {
    display: flex; align-items: center; gap: 10px;
    font-size: 14px; color: var(--text-dark); height: 26px;
  }
  .contacts svg { width: 15px; height: 15px; flex: none; }

  .tagline {
    position: absolute; left: 0; right: 0; top: 226px;
    text-align: center;
    font-size: 15px; letter-spacing: 0.06em;
    color: var(--paper); text-transform: uppercase;
  }
</style>
</head>
<body>
<main class="stage">
  <section class="card card-front" aria-label="Business card front">
    <h1 class="wordmark">Brindlewave Capital</h1>
    <div class="holder">
      <p class="holder-name">Gregory Tallis</p>
      <p class="holder-title">Managing Partner</p>
    </div>
    <span class="divider"></span>
    <ul class="contacts">
      <li>
        <svg viewBox="0 0 16 16" aria-hidden="true"><path fill="#4383c6" d="M3.6 1.5l2.2 2.6-1.3 1.6c.8 1.9 2.1 3.3 3.9 4.1l1.6-1.3 2.6 2.2-1.3 2.6C6.4 13.1 2.9 9.6 2.7 3l.9-1.5z"/></svg>
        (628)354-xxxx
      </li>
      <li>
        <svg viewBox="0 0 16 16" aria-hidden="true"><rect x="1" y="3" width="14" height="10" rx="1" fill="#4383c6"/><path d="M1.5 3.8L8 9l6.5-5.2" fill="none" stroke="#fff" stroke-width="1.2"/></svg>
        gtallis@brindlewave.vc
      </li>
      <li>
        <svg viewBox="0 0 16 16" aria-hidden="true"><circle cx="8" cy="8" r="6.5" fill="none" stroke="#4383c6" stroke-width="1.3"/><ellipse cx="8" cy="8" rx="2.8" ry="6.5" fill="none" stroke="#4383c6" stroke-width="1"/><path d="M1.5 8h13M2.6 4.6h10.8M2.6 11.4h10.8" stroke="#4383c6" stroke-width="1"/></svg>
        www.brindlewave.vc
      </li>
    </ul>
  </section>

  <section class="card card-back" aria-label="Business card back">
    <h2 class="wordmark">Brindlewave Capital</h2>
    <p class="tagline">Transforming Traditional Industry</p>
  </section>
</main>
</body>
</html>
```